Business Card Design REAL ESTATE SALES PLEASE DESIGN MY CARD 2COLOR CARD WITH RED AS THE DOMINANT

FERNHOLM REALTY
TorLPA Lic# 04738216
RAFAEL " RAFE " MORTON Tel 555 218-3396
TorLPA Lic# 02864057 Fax 555 218-3740
Email: rafe@rafemortonhomes.net Cell 555 902-4481
47530 WREN TERRACE UNION CITY, CA 94312

RAFAEL " RAFE " MORTON
TEL: 555 218-3396 FAX 555 218-3740
Address: 47530 Wren Terrace Larkhaven , NV
EMAIL ADDRESS: rafe@rafemortonhomes.net

```html
<!DOCTYPE html>
<html lang="en">
<head>
<meta charset="utf-8">
<title>Fernholm Realty – Business Card</title>
<link rel="stylesheet" href="https://fonts.googleapis.com/css2?family=Montserrat:wght@400;600;700&family=Lato:wght@400&display=swap">
<style>
  :root {
    --bg: #e9e6e2;
    --ink-dark: #1c1c1d;
    --ink-mid: #3e3e40;
    --red: #d5202f;
    --red-deep: #b3141f;
    --white: #ffffff;
    --grey-text: #555558;
    --body-text: #2a2a2a;
  }
  * { box-sizing: border-box; margin: 0; padding: 0; }
  html, body { width: 1200px; height: 913px; overflow: hidden; }
  body {
    background: var(--bg);
    font-family: "Lato", sans-serif;
    position: relative;
  }
  .card {
    position: absolute;
    width: 540px;
    height: 309px;
    border-radius: 4px;
    overflow: hidden;
    box-shadow: 0 10px 28px rgba(0,0,0,.22);
  }
  /* Front */
  .card--front { left: 40px; top: 302px;
    background: linear-gradient(160deg, #555557 0%, var(--ink-mid) 35%, var(--ink-dark) 100%); }
  .card--front .brand {
    position: absolute; left: 0; right: 0; top: 96px;
    display: flex; align-items: center; justify-content: center; gap: 12px;
  }
  .brand__mark { width: 16px; height: 16px; background: var(--red); flex: none; }
  .brand__name {
    font-family: "Montserrat", sans-serif; font-weight: 400;
    font-size: 28px; letter-spacing: 3px; color: var(--white);
    white-space: nowrap;
  }
  .card--front .band {
    position: absolute; left: 0; right: 0; bottom: 0; height: 86px;
    background: linear-gradient(180deg, var(--red) 0%, var(--red-deep) 100%);
    display: flex; align-items: center; justify-content: center;
  }
  .licence { color: var(--white); font-size: 15px; letter-spacing: .5px; }

  /* Back */
  .card--back { left: 620px; top: 302px; background: var(--white); }
  .logo-panel {
    position: absolute; left: 0; top: 38px; width: 236px; height: 124px;
    background: linear-gradient(160deg, #4a4a4c 0%, var(--ink-dark) 100%);
    border-radius: 0 10px 10px 0;
    display: flex; align-items: center; justify-content: center; gap: 8px;
  }
  .logo-panel .brand__mark { width: 10px; height: 10px; }
  .logo-panel .brand__name { font-size: 15px; letter-spacing: 2px; }
  .agent-name {
    position: absolute; left: 258px; top: 68px;
    font-family: "Montserrat", sans-serif; font-weight: 700;
    font-size: 17px; color: var(--grey-text); letter-spacing: .3px;
    white-space: nowrap;
  }
  .contact {
    position: absolute; display: flex; align-items: center; gap: 7px;
    font-size: 12.5px; line-height: 15px; color: var(--body-text);
    white-space: nowrap;
  }
  .contact svg { width: 12px; height: 12px; flex: none; fill: var(--body-text); }
  .contact--email { left: 258px; top: 142px; }
  .contact--tel { left: 20px; top: 176px; }
  .contact--fax { left: 20px; top: 194px; }
  .card--back .band {
    position: absolute; left: 0; right: 0; bottom: 0; height: 86px;
    background: linear-gradient(180deg, var(--red) 0%, var(--red-deep) 100%);
  }
  .contact--address { left: 20px; top: 30px; color: var(--white); font-size: 13px; }
  .contact--address svg { fill: var(--white); }
</style>
</head>
<body>
  <section class="card card--front" aria-label="Card front">
    <div class="brand">
      <span class="brand__mark"></span>
      <span class="brand__name">FERNHOLM REALTY</span>
    </div>
    <div class="band"><p class="licence">TorLPA Lic# 02864057</p></div>
  </section>

  <section class="card card--back" aria-label="Card back">
    <div class="logo-panel">
      <span class="brand__mark"></span>
      <span class="brand__name">FERNHOLM REALTY</span>
    </div>
    <h1 class="agent-name">RAFAEL " RAFE " MORTON</h1>
    <p class="contact contact--email">
      <svg viewBox="0 0 12 12"><path d="M0 2h12v8H0z M0 2l6 4 6-4" fill="none" stroke="#2a2a2a" stroke-width="1.2"/></svg>
      rafe@rafemortonhomes.net
    </p>
    <p class="contact contact--tel">
      <svg viewBox="0 0 12 12"><path d="M1 3c0-1 1-2 2-2h6c1 0 2 1 2 2v1H8V3H4v1H1z M3 5h6l2 6H1z"/></svg>
      (555) 218-3396
    </p>
    <p class="contact contact--fax">
      <svg viewBox="0 0 12 12"><path d="M3 1h6v3H3z M1 5h10v5H1z M3 8h6v3H3z"/></svg>
      (555) 218-3740
    </p>
    <div class="band">
      <p class="contact contact--address">
        <svg viewBox="0 0 12 12"><path d="M6 0a4 4 0 0 0-4 4c0 3 4 8 4 8s4-5 4-8a4 4 0 0 0-4-4zm0 5.5a1.5 1.5 0 1 1 0-3 1.5 1.5 0 0 1 0 3z"/></svg>
        47530 Wren Terrace Larkhaven , NV
      </p>
    </div>
  </section>
</body>
</html>
```